Veltrano - Mechanic/Collision Center Business Card

We're looking for a business card design for our mechanic/ collision repair shop.

Can be with colours or monochromatic.

See the attached files.

Many thanks

```html
<!DOCTYPE html>
<html lang="pt">
<head>
<meta charset="utf-8">
<title>Veltrano – Business Card</title>
<link href="https://fonts.googleapis.com/css2?family=Lato:wght@400;700;900&display=swap" rel="stylesheet">
<style>
  :root {
    --stage: #2b2b2d;
    --brand-blue: #1673a0;
    --brand-blue-light: #2a8cc0;
    --ink-dark: #1b2530;
    --text-grey: #2f3338;
    --paper: #ffffff;
    --rule: #7fb3cf;
  }
  * { margin: 0; padding: 0; box-sizing: border-box; }
  html, body {
    width: 1200px; height: 878px; overflow: hidden;
    background: var(--stage);
    font-family: "Lato", sans-serif;
  }
  .stage { position: relative; width: 1200px; height: 878px; }

  .card {
    position: absolute;
    width: 620px; height: 354px;
    left: 290px;
    overflow: hidden;
    box-shadow: 0 14px 30px rgba(0,0,0,.45);
  }

  /* Back side */
  .card-back { top: 50px; background: var(--brand-blue); }
  .card-back .brand-name {
    position: absolute; left: 0; right: 0; top: 50%;
    transform: translateY(-50%);
    text-align: center;
    font-weight: 900; font-size: 64px; letter-spacing: 2px;
    color: var(--ink-dark);
  }

  /* Front side */
  .card-front { top: 460px; background: var(--paper); }
  .identity { position: absolute; left: 40px; top: 30px; }
  .identity .company {
    font-weight: 900; font-size: 22px; color: var(--brand-blue);
  }
  .identity .role {
    font-size: 13px; color: var(--text-grey); margin-top: 1px;
  }

  .front-logo {
    position: absolute; right: 40px; top: 128px;
    display: flex; align-items: center; gap: 12px;
  }
  .front-logo .mark-square {
    width: 26px; height: 26px; background: var(--brand-blue);
  }
  .front-logo .brand-name {
    font-weight: 900; font-size: 42px; letter-spacing: 1px;
    color: var(--ink-dark);
  }

  .contacts {
    position: absolute; left: 40px; top: 196px;
    list-style: none;
  }
  .contacts li {
    display: flex; align-items: center; gap: 12px;
    font-size: 17px; color: var(--text-grey);
    height: 24px;
  }
  .contacts svg { width: 14px; height: 14px; fill: var(--brand-blue); flex: none; }

  .divider {
    position: absolute; left: 34px; right: 64px; height: 1px;
    background: var(--rule);
  }
  .divider-top { top: 272px; }
  .divider-bottom { top: 312px; }

  .address {
    position: absolute; left: 40px; top: 280px;
    display: flex; align-items: center; gap: 12px;
    font-size: 17px; color: var(--text-grey);
  }
  .address svg { width: 14px; height: 16px; fill: var(--brand-blue); }

  .footer-band {
    position: absolute; left: 0; right: 0; bottom: 0; height: 18px;
    background: var(--brand-blue);
  }
  .footer-tab {
    position: absolute; left: 0; bottom: 0; width: 46px; height: 18px;
    background: var(--ink-dark);
    border-right: 5px solid var(--paper);
  }
</style>
</head>
<body>
<main class="stage">

  <section class="card card-back" aria-label="Business card back">
    <div class="brand-name">VELTRANO</div>
  </section>

  <section class="card card-front" aria-label="Business card front">
    <div class="identity">
      <div class="company">Veltrano, LDA</div>
      <div class="role">Founder &amp; CEO</div>
    </div>

    <div class="front-logo">
      <span class="mark-square"></span>
      <span class="brand-name">VELTRANO</span>
    </div>

    <ul class="contacts">
      <li>
        <svg viewBox="0 0 24 24"><path d="M6.6 10.8a15.1 15.1 0 0 0 6.6 6.6l2.2-2.2c.3-.3.7-.4 1-.2 1.1.4 2.3.6 3.6.6.6 0 1 .4 1 1V20c0 .6-.4 1-1 1A17 17 0 0 1 3 4c0-.6.4-1 1-1h3.5c.6 0 1 .4 1 1 0 1.3.2 2.5.6 3.6.1.3 0 .7-.2 1z"/></svg>
        +351 210 555 014
      </li>
      <li>
        <svg viewBox="0 0 24 24"><path d="M2 5h20v14H2z M2 5l10 8 10-8" fill="none" stroke="#1673a0" stroke-width="2.2"/></svg>
        oficina@veltrano-auto.pt
      </li>
      <li>
        <svg viewBox="0 0 24 24"><circle cx="12" cy="12" r="9.5" fill="none" stroke="#1673a0" stroke-width="2"/><path d="M2.5 12h19M12 2.5c3 3 3 16 0 19M12 2.5c-3 3-3 16 0 19" fill="none" stroke="#1673a0" stroke-width="1.6"/></svg>
        www.veltrano-auto.pt
      </li>
    </ul>

    <div class="divider divider-top"></div>

    <div class="address">
      <svg viewBox="0 0 24 28"><path d="M12 0a9 9 0 0 0-9 9c0 7 9 19 9 19s9-12 9-19a9 9 0 0 0-9-9zm0 12.5A3.5 3.5 0 1 1 12 5.5a3.5 3.5 0 0 1 0 7z"/></svg>
      Rua das Oficinas, 12 1900-100 Lisboa
    </div>

    <div class="divider divider-bottom"></div>

    <div class="footer-band"></div>
    <div class="footer-tab"></div>
  </section>

</main>
</body>
</html>
```